Asphalt Driveway Billboard Design

We need a billboard designed for an Asphalt & Concrete Company in Minnesota. We want to advertise Asphalt Driveways on this billboard! Logo is uploaded below. Our website is tamlin-paving.com for more information.

```html
<!DOCTYPE html>
<html lang="en">
<head>
<meta charset="utf-8">
<title>Tamlin Paving – Billboard</title>
<link href="https://fonts.googleapis.com/css2?family=Montserrat:wght@600;800&family=Oswald:wght@600&display=swap" rel="stylesheet">
<style>
  :root{
    --page:#e4ecf4;
    --dark:#272727;
    --white:#ffffff;
    --green:#38c96a;
    --green-ink:#161616;
    --blue-top:#1a73c4;
    --blue-bottom:#0a4c92;
    --blue-word:#4f94dc;
  }
  html,body{margin:0;padding:0;overflow:hidden}
  body{width:1200px;height:1196px;background:var(--page);position:relative}

  .board{position:absolute;left:50px;width:1100px;height:317px;overflow:hidden;box-shadow:0 6px 18px rgba(0,0,0,.18)}
  .board--green{top:190px;--accent:var(--green);--ink:var(--green-ink);--word:var(--green)}
  .board--blue{top:690px;--accent:url(#blueFill);--ink:var(--white);--word:var(--blue-word)}

  .board__art{position:absolute;inset:0;width:100%;height:100%}
  .fill-dark{fill:var(--dark)}
  .fill-white{fill:var(--white)}
  .board--green .fill-accent{fill:var(--green)}
  .board--blue .fill-accent{fill:url(#blueFill)}
  .divider{stroke:var(--white);stroke-width:2.5}

  .brand{position:absolute;left:0;top:70px;width:360px;text-align:center;font-family:"Montserrat",sans-serif;font-weight:800;color:var(--dark);line-height:1}
  .brand__name{font-size:56px;letter-spacing:1px}
  .brand__tag{font-size:15px;letter-spacing:2px;margin-top:10px}

  .url{position:absolute;left:0;top:272px;width:380px;height:45px;line-height:45px;text-align:center;font-family:"Montserrat",sans-serif;font-weight:600;font-size:18px;letter-spacing:.6px;color:var(--white)}

  .headline{position:absolute;left:446px;top:12px;margin:0;font-family:"Oswald",sans-serif;font-weight:600;font-size:44px;line-height:54px;color:var(--white);white-space:nowrap;letter-spacing:.2px}
  .headline__word{color:var(--word)}

  .services{position:absolute;left:446px;top:92px;margin:0;padding:0;list-style:none;font-family:"Montserrat",sans-serif;font-weight:800;font-size:24px;color:var(--ink);white-space:nowrap}
  .services li{display:flex;align-items:center;height:35.5px}
  .tick{width:22px;height:22px;margin-right:12px;flex:none}
  .tick path,.tick rect{fill:none;stroke:var(--ink);stroke-width:2.6;stroke-linecap:round;stroke-linejoin:round}

  .cta{position:absolute;left:446px;top:258px;height:54px;display:flex;align-items:center;color:var(--ink);white-space:nowrap}
  .cta__big{font-family:"Oswald",sans-serif;font-weight:600;font-size:40px;line-height:1}
  .cta__stack{display:flex;flex-direction:column;font-family:"Montserrat",sans-serif;font-weight:600;font-size:14px;line-height:14px;margin:0 6px;text-transform:uppercase}
  .cta__icon{width:26px;height:26px;margin:0 10px 0 12px}
  .cta__icon circle{fill:var(--ink)}
  .cta__icon path{fill:var(--accent-icon,#fff)}
  .board--green .cta__icon path{fill:var(--green)}
  .board--blue .cta__icon path{fill:var(--blue-bottom)}
  .cta__phone{font-family:"Montserrat",sans-serif;font-weight:800;font-size:38px;line-height:1}
</style>
</head>
<body>
<svg width="0" height="0" style="position:absolute" aria-hidden="true">
  <defs>
    <linearGradient id="blueFill" x1="0" y1="0" x2="1" y2="1">
      <stop offset="0" stop-color="#1a73c4"/>
      <stop offset="1" stop-color="#0a4c92"/>
    </linearGradient>
  </defs>
</svg>

<!-- Green variant -->
<section class="board board--green" aria-label="Billboard, green version">
  <svg class="board__art" viewBox="0 0 1100 317" preserveAspectRatio="none" aria-hidden="true">
    <rect class="fill-accent" width="1100" height="317"/>
    <rect class="fill-dark" width="1100" height="78"/>
    <path class="fill-white" d="M0 0H318C395 60 420 190 400 317H0Z"/>
    <path class="fill-accent" d="M0 0H300C378 55 405 185 394 317H0Z"/>
    <path class="fill-dark" d="M0 0H205C320 40 392 170 388 317H0Z"/>
    <path class="fill-white" d="M0 0H172C290 40 370 160 380 272H0Z"/>
    <line class="divider" x1="412" y1="246" x2="1100" y2="244"/>
  </svg>
  <div class="brand"><div class="brand__name">TAMLIN</div><div class="brand__tag">PAVING &amp; CONCRETE</div></div>
  <div class="url">WWW.TAMLIN-PAVING.COM</div>
  <h2 class="headline">SERVING ALL YOUR <span class="headline__word">ASPHALT</span> NEEDS</h2>
  <ul class="services">
    <li><svg class="tick" viewBox="0 0 22 22"><rect x="2" y="4" width="15" height="15" rx="2"/><path d="M6 11l4 4 9-11"/></svg>RESIDENTIAL ASPHALT DRIVEWAY</li>
    <li><svg class="tick" viewBox="0 0 22 22"><rect x="2" y="4" width="15" height="15" rx="2"/><path d="M6 11l4 4 9-11"/></svg>ASPHALT ADDITIONS</li>
    <li><svg class="tick" viewBox="0 0 22 22"><rect x="2" y="4" width="15" height="15" rx="2"/><path d="M6 11l4 4 9-11"/></svg>ASPHALT SEALCOATING &amp; CRACK FILLING</li>
    <li><svg class="tick" viewBox="0 0 22 22"><rect x="2" y="4" width="15" height="15" rx="2"/><path d="M6 11l4 4 9-11"/></svg>ASPHALT PARKING LOTS</li>
  </ul>
  <div class="cta">
    <span class="cta__big">CALL</span>
    <span class="cta__stack"><span>for</span><span>your</span></span>
    <span class="cta__big">FREE</span>
    <span class="cta__stack"><span>asphalt</span><span>estimate</span></span>
    <svg class="cta__icon" viewBox="0 0 26 26"><circle cx="13" cy="13" r="13"/><path d="M8.5 6.5l2.6-.3 1.3 3.4-1.6 1.2a8 8 0 0 0 4.4 4.4l1.2-1.6 3.4 1.3-.3 2.6c-.2 1-1 1.6-2 1.5A12 12 0 0 1 7 8.5c-.1-1 .5-1.8 1.5-2Z"/></svg>
    <span class="cta__phone">763-555-0148</span>
  </div>
</section>

<!-- Blue variant -->
<section class="board board--blue" aria-label="Billboard, blue version">
  <svg class="board__art" viewBox="0 0 1100 317" preserveAspectRatio="none" aria-hidden="true">
    <rect class="fill-accent" width="1100" height="317"/>
    <rect class="fill-dark" width="1100" height="78"/>
    <path class="fill-white" d="M0 0H318C395 60 420 190 400 317H0Z"/>
    <path class="fill-accent" d="M0 0H300C378 55 405 185 394 317H0Z"/>
    <path class="fill-dark" d="M0 0H205C320 40 392 170 388 317H0Z"/>
    <path class="fill-white" d="M0 0H172C290 40 370 160 380 272H0Z"/>
    <line class="divider" x1="412" y1="246" x2="1100" y2="244"/>
  </svg>
  <div class="brand"><div class="brand__name">TAMLIN</div><div class="brand__tag">PAVING &amp; CONCRETE</div></div>
  <div class="url">WWW.TAMLIN-PAVING.COM</div>
  <h2 class="headline">SERVING ALL YOUR <span class="headline__word">ASPHALT</span> NEEDS</h2>
  <ul class="services">
    <li><svg class="tick" viewBox="0 0 22 22"><rect x="2" y="4" width="15" height="15" rx="2"/><path d="M6 11l4 4 9-11"/></svg>RESIDENTIAL ASPHALT DRIVEWAY</li>
    <li><svg class="tick" viewBox="0 0 22 22"><rect x="2" y="4" width="15" height="15" rx="2"/><path d="M6 11l4 4 9-11"/></svg>ASPHALT ADDITIONS</li>
    <li><svg class="tick" viewBox="0 0 22 22"><rect x="2" y="4" width="15" height="15" rx="2"/><path d="M6 11l4 4 9-11"/></svg>ASPHALT SEALCOATING &amp; CRACK FILLING</li>
    <li><svg class="tick" viewBox="0 0 22 22"><rect x="2" y="4" width="15" height="15" rx="2"/><path d="M6 11l4 4 9-11"/></svg>ASPHALT PARKING LOTS</li>
  </ul>
  <div class="cta">
    <span class="cta__big">CALL</span>
    <span class="cta__stack"><span>for</span><span>your</span></span>
    <span class="cta__big">FREE</span>
    <span class="cta__stack"><span>asphalt</span><span>estimate</span></span>
    <svg class="cta__icon" viewBox="0 0 26 26"><circle cx="13" cy="13" r="13"/><path d="M8.5 6.5l2.6-.3 1.3 3.4-1.6 1.2a8 8 0 0 0 4.4 4.4l1.2-1.6 3.4 1.3-.3 2.6c-.2 1-1 1.6-2 1.5A12 12 0 0 1 7 8.5c-.1-1 .5-1.8 1.5-2Z"/></svg>
    <span class="cta__phone">763-555-0148</span>
  </div>
</section>
</body>
</html>
```